Travel Consultant Business Card

Hello.. New travel consultant looking seeking a business card that incorporates my new logo. I specialize in cruises but also want to imply land vacation. I am very open to any design and font concepts. I'm looking for a very upbeat modern design that reflects cruise and land vacations. Bright vibrant colors

Target Market(s)

Cruise and Land Vacationers

Industry/Entity Type

Travel Agent

Contact Information for Business Card

I am very open to any design and font concepts. I'm looking for a very upbeat modern design that reflects cruise and land vacations. Bright vibrant colors

Colors

Designer to choose colors to be used in the design.

Requirements
Must have
• Company Name: MapleRidge Journeys---New logo uploaded to be included in design
• My Name: Dolores Kwiatek-Travel Consultant
• Phone Number: (555) 418-7093
• E-Mail Address: mapleridgejourneys@examplemail.net
• Website: www.mapleridgejourneys.example
Nice to have
• My tag line is …..Here to Get You There

```html
<!DOCTYPE html>
<html lang="en">
<head>
<meta charset="utf-8">
<title>MapleRidge Journeys – Business Card</title>
<link href="https://fonts.googleapis.com/css2?family=Roboto:wght@400;700&family=Roboto+Condensed:wght@700&display=swap" rel="stylesheet">
<style>
  :root {
    --backdrop: #2b2b2b;
    --sky: #00aeef;
    --navy: #0358a8;
    --white: #ffffff;
    --ink-grey: #555555;
  }
  html, body {
    margin: 0;
    padding: 0;
    width: 1200px;
    height: 1200px;
    overflow: hidden;
    background: var(--backdrop);
  }
  .canvas {
    position: relative;
    width: 1200px;
    height: 1200px;
  }
  .card {
    position: absolute;
    left: 217px;
    width: 800px;
    height: 457px;
    overflow: hidden;
    box-shadow: 0 3px 8px rgba(0,0,0,0.45);
  }
  .card--front {
    top: 115px;
    background: var(--sky);
  }
  .card--back {
    top: 637px;
    background: var(--white);
  }
  .front__band {
    position: absolute;
    left: 0;
    top: 0;
    width: 250px;
    height: 100%;
    background: var(--navy);
  }
  .front__mark {
    position: absolute;
    left: 40px;
    top: 60px;
    width: 420px;
    height: 340px;
    display: flex;
    flex-direction: column;
    align-items: center;
    justify-content: center;
    gap: 18px;
  }
  .front__mark-dot {
    width: 150px;
    height: 150px;
    border-radius: 50%;
    background: var(--white);
    opacity: 0.9;
  }
  .front__mark-name {
    margin: 0;
    font-family: "Roboto", sans-serif;
    font-weight: 700;
    font-size: 40px;
    line-height: 46px;
    color: var(--white);
    text-align: center;
  }
  .front__details {
    position: absolute;
    right: 45px;
    top: 252px;
    text-align: right;
    font-family: "Roboto", sans-serif;
    color: var(--white);
  }
  .holder-name {
    margin: 0;
    font-family: "Roboto Condensed", sans-serif;
    font-weight: 700;
    font-size: 31px;
    line-height: 36px;
    color: var(--navy);
    text-transform: uppercase;
  }
  .holder-role {
    margin: 0 0 16px;
    font-size: 21px;
    line-height: 26px;
  }
  .contact-list {
    list-style: none;
    margin: 0;
    padding: 0;
  }
  .contact-list li {
    display: flex;
    justify-content: flex-end;
    align-items: center;
    gap: 10px;
    font-size: 19px;
    line-height: 26px;
  }
  .contact-list svg {
    width: 18px;
    height: 18px;
    fill: var(--navy);
    flex: none;
  }
  .back__brand {
    position: absolute;
    left: 0;
    right: 0;
    top: 180px;
    text-align: center;
    font-family: "Roboto", sans-serif;
    font-weight: 700;
    font-size: 52px;
    line-height: 66px;
    color: var(--navy);
    margin: 0;
  }
  .back__web {
    position: absolute;
    left: 0;
    right: 0;
    top: 390px;
    text-align: center;
    font-family: "Roboto", sans-serif;
    font-size: 19px;
    letter-spacing: 0.3em;
    color: var(--ink-grey);
    margin: 0;
  }
</style>
</head>
<body>
<main class="canvas">
  <section class="card card--front">
    <div class="front__band"></div>
    <div class="front__mark">
      <div class="front__mark-dot"></div>
      <p class="front__mark-name">MapleRidge Journeys</p>
    </div>
    <div class="front__details">
      <h1 class="holder-name">Dolores Kwiatek</h1>
      <p class="holder-role">Travel Consultant</p>
      <ul class="contact-list">
        <li>(555) 418-7093
          <svg viewBox="0 0 24 24" aria-hidden="true"><path d="M6.6 10.8c1.4 2.8 3.8 5.1 6.6 6.6l2.2-2.2c.3-.3.7-.4 1-.2 1.1.4 2.3.6 3.6.6.6 0 1 .4 1 1V20c0 .6-.4 1-1 1C10.6 21 3 13.4 3 4c0-.6.4-1 1-1h3.5c.6 0 1 .4 1 1 0 1.2.2 2.4.6 3.6.1.3 0 .7-.2 1L6.6 10.8z"/></svg>
        </li>
        <li>mapleridgejourneys@examplemail.net
          <svg viewBox="0 0 24 24" aria-hidden="true"><path d="M2 5h20v14H2z M4 7v.5l8 5 8-5V7l-8 5z" fill-rule="evenodd"/></svg>
        </li>
        <li>www.mapleridgejourneys.example
          <svg viewBox="0 0 24 24" aria-hidden="true"><circle cx="12" cy="12" r="10"/><path d="M8 6c2 1 3 3 2 5s-3 2-3 4 M14 18c0-2 2-3 4-3" stroke="#00aeef" stroke-width="1.6" fill="none"/></svg>
        </li>
      </ul>
    </div>
  </section>

  <section class="card card--back">
    <p class="back__brand">MapleRidge Journeys</p>
    <p class="back__web">www.mapleridgejourneys.example</p>
  </section>
</main>
</body>
</html>
```